IT Consulting Firm Website
Core Values: Proficiency ♦ Consistency ♦ Integrity
IT Consulting Firm Website - Information Technology
Creative Brief
Information Technology
www.dunmorevantage.com
Premier IT Services Consulting firm with a heavy emphasis on ethical business practices and superior technical skillsets. Dunmore Consulting designs and implements effective solutions that are specific to the client's information technology issues and business model. Harness our ability to assess your information technology concerns and deliver a solution that meets the company's current requirements and plan appropriately for the company's future demands. DCHP understands how technology works and has a clear focus enabling us to accurately read the strategic big picture of any business challenge. Business continuity and disaster recovery plans are also addressed and implemented as part of the IT solution. Dunmore Consulting has led successful efforts in delivering effective IT solutions to difficult and complex business challenges.
we are looking for a website design that will establish our brand as professional, ethical and technically superior to our competitors. Nothing cartoonish. Something that will identify us by the solid and stable IT industry relationships we've developed.
Modern
Core color is Cobalt Blue (Pantone 288C - RGB 00337F)
RGB 1975FF
RGB 3F3F3F & RGB 000000
below header
Please use images from www.lumepixbank.com Also, please make sure you guys use our NEW logo that I've uploaded to the project and to design with that in mind. Not our old logo that you see on the website.

```html
<!DOCTYPE html>
<html lang="en">
<head>
<meta charset="utf-8">
<title>Dunmore Consulting</title>
<link rel="stylesheet" href="https://fonts.googleapis.com/css2?family=Open+Sans:wght@400;600;700&family=Cinzel:wght@600&display=swap">
<style>
:root{
  --cobalt:#00337f;
  --bright:#1975ff;
  --band:#1a73b8;
  --band-dark:#0d4f86;
  --charcoal:#3f3f3f;
  --black:#000;
  --paper:#fff;
  --page:#f2f2f2;
  --text:#333;
}
*{margin:0;padding:0;box-sizing:border-box}
html,body{width:1200px;height:901px;overflow:hidden}
body{background:var(--page);font-family:"Open Sans",Arial,sans-serif;color:var(--text);position:relative}
.site{position:absolute;left:150px;top:24px;width:900px;height:800px;background:var(--paper)}
.header{position:absolute;left:0;top:0;width:900px;height:192px;background:linear-gradient(90deg,#0a0a0a 0%,#2e2e2e 55%,var(--charcoal) 100%)}
.brand{position:absolute;left:100px;top:14px;width:240px;text-align:center;color:#fff}
.brand-mark{width:34px;height:34px;border-radius:50%;background:var(--bright);margin:0 auto 6px}
.brand-name{font-family:"Cinzel",serif;font-size:17px;letter-spacing:1px}
.tagline{position:absolute;left:78px;top:102px;color:#fff;font-size:10.5px;font-weight:700;letter-spacing:.6px}
.nav{position:absolute;left:445px;top:16px;width:270px;height:20px;background:#fff;border-radius:4px;display:flex;align-items:center;justify-content:space-around;padding:0 6px;font-size:8px;font-weight:600}
.nav a{color:var(--text);text-decoration:none;padding:2px 6px}
.nav a.active{background:var(--bright);color:#fff;border-radius:2px}
.hero{position:absolute;left:421px;top:46px;width:312px;height:141px;background:linear-gradient(135deg,#f4f5f7 0%,#b9c3cf 50%,#5d6e82 100%)}
.band{position:absolute;left:0;top:192px;width:900px;height:36px;background:linear-gradient(180deg,var(--band) 0%,var(--band-dark) 100%)}
.dots{position:absolute;left:565px;top:14px;display:flex;gap:5px}
.dots span{width:7px;height:7px;border-radius:50%;background:#fff}
.dots span:first-child{background:#9cc4ea}
.services{position:absolute;left:186px;top:240px;display:flex;gap:30px}
.service{width:156px;height:168px;background:#fff;box-shadow:0 1px 4px rgba(0,0,0,.25)}
.service h3{background:linear-gradient(180deg,var(--bright),var(--cobalt));color:#fff;font-size:8px;font-weight:700;text-align:center;padding:5px 0;letter-spacing:.3px}
.service ul{list-style:none;padding:10px 10px 0 14px;font-size:8.5px;line-height:13px}
.service li::before{content:"• ";color:var(--cobalt)}
.service .more{display:block;margin:8px auto 0;width:44px;background:#222;color:#fff;font-size:6px;text-align:center;padding:3px 0;border-radius:2px}
.section-title{position:absolute;font-size:10px;font-weight:700;color:var(--black)}
.clients{position:absolute;left:186px;top:468px;width:355px;height:58px;border-top:1px solid #ccc;border-bottom:1px solid #ccc;display:flex;align-items:center;justify-content:space-around;padding:0 22px}
.arrow{position:absolute;top:20px;width:16px;height:16px;border-radius:50%;background:#333}
.client{display:flex;align-items:center;gap:4px;font-size:10px;font-weight:700;color:var(--text)}
.client i{width:12px;height:12px;background:#777;border-radius:50%;display:inline-block}
.testimonial{position:absolute;left:556px;top:458px;width:158px;height:96px;background:#fff;box-shadow:0 1px 4px rgba(0,0,0,.25);padding:10px 10px 0 18px;font-size:7px;line-height:10px}
.testimonial b{position:absolute;left:5px;top:3px;font-size:20px;color:#333}
.footer{position:absolute;left:0;top:583px;width:900px;height:180px;background:linear-gradient(180deg,#2a7fc0,var(--band-dark))}
.fcol{position:absolute;top:8px;color:#fff;font-size:7px;line-height:10px}
.fcol h4{display:inline-block;background:#123a66;font-size:7.5px;padding:3px 7px;margin-bottom:8px}
.fcol p{margin-bottom:6px}
.blog{display:flex;gap:6px;margin-bottom:8px}
.thumb{width:22px;height:22px;background:linear-gradient(135deg,#d8dde3,#8e9aa7);flex:none}
.social{display:flex;gap:4px;margin-top:4px}
.social span{width:12px;height:12px;background:#dfe7ef}
.bottom{position:absolute;left:0;top:763px;width:900px;height:35px;background:#1b1b1b;color:#ccc;font-size:6.5px;text-align:center;padding-top:7px}
.bottom nav{display:flex;justify-content:center;gap:40px;margin-bottom:5px}
</style>
</head>
<body>
<div class="site">
  <header class="header">
    <div class="brand"><div class="brand-mark"></div><div class="brand-name">DUNMORE CONSULTING</div></div>
    <div class="tagline">PROFICIENCY - CONSISTENCY - INTEGRITY</div>
    <nav class="nav"><a class="active">HOME</a><a>About Us</a><a>SOLUTIONS</a><a>CAREERS</a><a>CONTACT US</a></nav>
    <div class="hero" role="img" aria-label="Puzzle pieces labelled implement, develop, analyze and design"></div>
  </header>
  <div class="band"><div class="dots"><span></span><span></span><span></span><span></span><span></span></div></div>

  <section class="services">
    <div class="service"><h3>NETWORK INTEGRATION</h3><ul><li>Infrastructure Analysis</li><li>Improved Scalability</li><li>Business Continuity</li><li>Assessment</li><li>Design &amp; Development</li></ul><span class="more">Read More</span></div>
    <div class="service"><h3>MANAGED I.T. SERVICES</h3><ul><li>Network Performance</li><li>Data Storage</li><li>Security Monitoring</li><li>Network Performance</li><li>Security Monitoring</li></ul><span class="more">Read More</span></div>
    <div class="service"><h3>CLOUD COMPUTING</h3><ul><li>Simplify IT Management</li><li>IT Services On Demand</li><li>Optimized Operational Efficiency</li><li>Assess Application Performance</li></ul><span class="more">Read More</span></div>
  </section>

  <h2 class="section-title" style="left:186px;top:440px">Our Clients</h2>
  <div class="clients">
    <span class="arrow" style="left:-8px"></span>
    <span class="client"><i></i>Delmar</span>
    <span class="client">Sonora</span>
    <span class="client">AeroVista</span>
    <span class="arrow" style="right:-8px"></span>
  </div>

  <h2 class="section-title" style="left:556px;top:440px">Testimonials</h2>
  <div class="testimonial"><b>“</b>Their team assessed our network quickly, delivered a clear plan and kept every promise. Our systems have run smoothly since the upgrade was completed.</div>

  <footer class="footer">
    <div class="fcol" style="left:186px;width:150px"><h4>Useful Resources</h4><p>Planning guide for secure network growth and upgrades</p><p>Checklist for business continuity and recovery</p><p>Overview of managed cloud service options</p></div>
    <div class="fcol" style="left:366px;width:150px"><h4>Contact Info</h4><p>Address: 120 Harbor Street, Suite 4</p><p>Email: info@dunmorevantage.com</p><p>Phone: (555) 014-2280</p><p>Fax: (555) 014-2281</p><p>Web: dunmorevantage.com</p>
      <h4 style="margin-top:4px">Follow Us</h4><div class="social"><span></span><span></span><span></span><span></span></div></div>
    <div class="fcol" style="left:553px;width:165px"><h4>Latest from Blog</h4>
      <div class="blog"><div class="thumb" role="img" aria-label="Blog post photo"></div><p>Notes on planning a network refresh without downtime this year</p></div>
      <div class="blog"><div class="thumb" role="img" aria-label="Blog post photo"></div><p>Why steady monitoring keeps small outages from growing</p></div></div>
  </footer>
  <div class="bottom"><nav><span>HOME</span><span>ABOUT US</span><span>COMPANY</span><span>SOLUTIONS</span><span>CAREERS</span><span>CONTACT US</span></nav>COPYRIGHT 2012 · ALL RIGHTS RESERVED</div>
</div>
</body>
</html>
```